Auto glass company

THRIFTWAY
Roving Auto Glass, LLC
555-604-1973

* Windshield Replacement
* Rock Chip Repair
Danny "K"
Thriftwayrovingautoglass@mailbox-demo.net
* Fully Insured

This is what I would like on the card. The image is what I had before. Looking for a logo possible too, couldn’t find a place to add that on. It’s a auto glass company.

Target Market(s)

Auto glass

Industry/Entity Type

Auto glass

Contact Information for Business Card

Logo, business name, phone number, windshield replacement, rock chip repair, insured, owner name Danny K, email address thriftwayrovingautoglass@mailbox-demo.net

Colors

Designer to choose colors to be used in the design.

Requirements
Must have
• Logo, business name, phone number, windshield replacement, rock chip repair, insured, owner name Danny K, email address thriftwayrovingautoglass@mailbox-demo.net

```html
<!DOCTYPE html>
<html lang="en">
<head>
<meta charset="utf-8">
<title>Kestrava Roving Auto Glass – Business Card</title>
<link href="https://fonts.googleapis.com/css2?family=Montserrat:wght@400;500;700;800&display=swap" rel="stylesheet">
<style>
  :root {
    --stage: #3a3a3c;
    --card: #1c1c1e;
    --white: #f2f2f2;
    --blue: #1f8ee0;
  }
  * { margin: 0; padding: 0; box-sizing: border-box; }
  html, body { width: 1200px; height: 1186px; overflow: hidden; }
  body {
    background: var(--stage);
    font-family: "Montserrat", sans-serif;
    position: relative;
  }
  .card {
    position: absolute;
    left: 150px;
    width: 900px;
    height: 514px;
    background: var(--card);
    border-radius: 30px;
    box-shadow: 0 18px 40px rgba(0,0,0,.45);
    overflow: hidden;
  }
  .card--front { top: 56px; }
  .card--back { top: 616px; }

  .brand { display: flex; align-items: center; gap: 22px; color: var(--white); font-weight: 700; }
  .brand__mark { width: 58px; height: 58px; background: var(--blue); flex: none; }
  .brand__name { font-size: 64px; letter-spacing: 3px; line-height: 1; }
  .brand__sub { font-size: 21px; letter-spacing: 3px; margin-top: 10px; text-transform: uppercase; }

  .card--front .brand { position: absolute; left: 0; right: 0; top: 150px; justify-content: center; }

  .services {
    position: absolute; left: 60px; right: 60px; bottom: 70px;
    display: flex; justify-content: space-between;
    list-style: none; color: var(--white); font-size: 22px; font-weight: 400;
  }
  .services li { display: flex; align-items: center; gap: 12px; }
  .services li::before { content: ""; width: 8px; height: 8px; border-radius: 50%; background: var(--blue); }

  .card--back .brand { position: absolute; right: 70px; top: 70px; gap: 16px; }
  .card--back .brand__mark { width: 44px; height: 44px; }
  .card--back .brand__name { font-size: 46px; }
  .card--back .brand__sub { font-size: 15px; margin-top: 8px; }

  .divider { position: absolute; left: 60px; right: 70px; top: 268px; height: 2px; background: var(--blue); }

  .person { position: absolute; left: 60px; top: 300px; }
  .person__name { color: var(--blue); font-size: 38px; font-weight: 800; }
  .person__role { color: var(--white); font-size: 20px; margin-top: 4px; }

  .contact { position: absolute; left: 60px; top: 408px; list-style: none; color: var(--white); font-size: 20px; }
  .contact li { display: flex; align-items: center; gap: 14px; margin-bottom: 12px; }
  .contact svg { width: 20px; height: 20px; fill: var(--blue); flex: none; }
</style>
</head>
<body>
  <section class="card card--front">
    <div class="brand">
      <span class="brand__mark"></span>
      <div>
        <div class="brand__name">KESTRAVA</div>
        <div class="brand__sub">Roving Auto Glass, LLC</div>
      </div>
    </div>
    <ul class="services">
      <li>Windshield Replacement</li>
      <li>Rock Chip Repair</li>
      <li>Fully Insured</li>
    </ul>
  </section>

  <section class="card card--back">
    <div class="brand">
      <span class="brand__mark"></span>
      <div>
        <div class="brand__name">KESTRAVA</div>
        <div class="brand__sub">Roving Auto Glass, LLC</div>
      </div>
    </div>
    <div class="divider"></div>
    <div class="person">
      <div class="person__name">Danny "K"</div>
      <div class="person__role">CEO &amp; Founder</div>
    </div>
    <ul class="contact">
      <li>
        <svg viewBox="0 0 24 24"><path d="M6.6 10.8a15.1 15.1 0 0 0 6.6 6.6l2.2-2.2a1 1 0 0 1 1-.25 11.4 11.4 0 0 0 3.6.57 1 1 0 0 1 1 1V20a1 1 0 0 1-1 1A17 17 0 0 1 3 4a1 1 0 0 1 1-1h3.5a1 1 0 0 1 1 1c0 1.25.2 2.45.57 3.57a1 1 0 0 1-.25 1z"/></svg>
        555-604-1973
      </li>
      <li>
        <svg viewBox="0 0 24 24"><path d="M2 5h20v14H2z M2 5l10 8 10-8" fill="none" stroke="#1f8ee0" stroke-width="2"/></svg>
        Kestravarovingautoglass@mailbox-demo.net
      </li>
    </ul>
  </section>
</body>
</html>
```